Whiskey Glass Packaging Design Project

I require a package design for my products - Whiskey Tasting glasses ( Set of 4) I will be selling on the Brindlecart USA platform. Must be of high quality, something that the customer will be very impressed with after opening once it arrives at their doorstop. To get an idea of competition please take a look on Brindlecart.example and do a search on Whiskey Glasses - Scotch Glasses. The competition is very good so we require something that will be better than them. We have a home and kitchen brand that caters to an audience that appreciate fine whiskey / oak barrels / cigars ... I can provide logo and content to be placed on box as well as dine line.

Target Market(s)

Men who love all things about Whiskey / Business / Cigars. Men / Women / Wives / Husbands who are looking to buy gifts for Husband / Partner .

Requirements
Must have
• On one side of the box we would like for the following wording to be included.
The GARVELOT snifter glass is one of the ideal glasses that all enthusiasts will swear by. The glass is a type of stemware, a short - stemmed glass whose vessel has a wide bottom and a relatively narrow top. It is mostly used to serve aged brown Scotch / Whiskey, Bourbon and Brandy.
It's simply a matter of raising the glass to take in a whiff of the aromas before taking a sip. We hope the graceful design of this GARVELOT Whiskey glass adds a nice touch of class to the presentation of your favourite drop ! Enjoy !
Nice to have
• Elegant, soothing and relaxing feel.
Should not have
• Nothing aggressive, racist, homosexual / anti gay .

```html
<!DOCTYPE html>
<html lang="en">
<head>
<meta charset="utf-8">
<title>GARVELOT Whiskey Glass Box – Panels</title>
<link href="https://fonts.googleapis.com/css2?family=Gabriela&family=Montserrat:wght@500&display=swap" rel="stylesheet">
<style>
  :root {
    --page-bg: #ecebee;
    --lid-purple: #4a3f5a;
    --pattern-dark: #231f22;
    --pattern-purple: #4b4163;
    --side-grey: #dcdbdd;
    --side-light: #f2f2f3;
    --whiskey-amber: #e7c774;
    --logo-orange: #e99a2c;
    --frame-white: #ffffff;
    --ink: #1d1b1c;
  }
  html, body {
    margin: 0;
    width: 1200px;
    height: 1087px;
    overflow: hidden;
    background: var(--page-bg);
  }
  .box-layout {
    position: absolute;
    left: 150px;
    top: 213px;
    width: 900px;
    height: 660px;
  }
  .panel {
    position: absolute;
    box-sizing: border-box;
  }
  .panel-lid {
    left: 300px;
    top: 0;
    width: 600px;
    height: 330px;
    background: var(--lid-purple);
  }
  .panel-side {
    left: 0;
    top: 330px;
    width: 300px;
    height: 330px;
    background: linear-gradient(90deg, var(--side-grey), var(--side-light));
    overflow: hidden;
  }
  .side-photo {
    position: absolute;
    left: 0;
    top: 0;
    width: 130px;
    height: 330px;
    background:
      linear-gradient(180deg, rgba(255,255,255,0) 0%, rgba(255,255,255,0) 45%, var(--whiskey-amber) 60%, rgba(231,199,116,0.35) 72%, rgba(220,219,221,0) 90%),
      linear-gradient(90deg, #cfced1, #e6e5e8);
  }
  .side-copy {
    position: absolute;
    left: 22px;
    top: 150px;
    width: 265px;
    margin: 0;
    font-family: "Gabriela", serif;
    font-size: 15px;
    line-height: 1.2;
    color: var(--ink);
  }
  .panel-front {
    left: 300px;
    top: 330px;
    width: 600px;
    height: 330px;
    background: repeating-linear-gradient(45deg, var(--pattern-dark) 0 9px, var(--pattern-purple) 9px 16px);
  }
  .brand-tile {
    position: absolute;
    left: 50%;
    top: 50%;
    width: 116px;
    height: 116px;
    transform: translate(-50%, -50%);
    background: var(--pattern-dark);
    border: 3px solid var(--frame-white);
    display: flex;
    align-items: center;
    justify-content: center;
  }
  .brand-name {
    font-family: "Montserrat", sans-serif;
    font-weight: 500;
    font-size: 11px;
    letter-spacing: 3px;
    color: var(--logo-orange);
    margin: 0;
  }
</style>
</head>
<body>
  <main class="box-layout">
    <section class="panel panel-lid" aria-label="Box lid"></section>

    <section class="panel panel-side" aria-label="Box side panel">
      <div class="side-photo" role="img" aria-label="Photograph of snifter glasses filled with whiskey"></div>
      <p class="side-copy">The GARVELOT snifter glass is one of the ideal glasses that all enthusiasts will swear by.</p>
    </section>

    <section class="panel panel-front" role="img" aria-label="Geometric nested zigzag pattern in dark purple and black">
      <div class="brand-tile">
        <p class="brand-name">GARVELOT</p>
      </div>
    </section>
  </main>
</body>
</html>
```